Carpet cleaning company wants business card

Need an exciting new fresh design for business cards for my carpet cleaning /pest control business
www.brightwovecare.com.au
Can design include a lined section for quoting or information? Thanks !

```html
<!DOCTYPE html>
<html lang="en">
<head>
<meta charset="utf-8">
<title>BrightWove Care – Business Card</title>
<link href="https://fonts.googleapis.com/css2?family=Montserrat:wght@400;600;800&display=swap" rel="stylesheet">
<style>
  :root {
    --brand-blue: #0c55a3;
    --brand-red: #e63b35;
    --ink: #1d1d1f;
    --paper: #ffffff;
    --backdrop: #2b3440;
  }
  * { box-sizing: border-box; margin: 0; padding: 0; }
  html, body {
    width: 1200px; height: 900px; overflow: hidden;
    background: var(--backdrop);
    font-family: "Montserrat", sans-serif;
  }
  .canvas { position: relative; width: 1200px; height: 900px; }
  .card {
    position: absolute; left: 300px; width: 600px; height: 360px;
    border-radius: 14px; overflow: hidden;
  }
  .card--front { top: 60px; background: var(--paper); }
  .card--back { top: 480px; background: var(--brand-blue); display: flex; align-items: center; justify-content: center; }

  .brand-name {
    position: absolute; left: 41px; top: 40px;
    font-weight: 800; font-size: 40px; letter-spacing: -1px;
    color: var(--brand-blue);
  }
  .brand-name--reverse {
    position: static; font-size: 62px; color: var(--paper);
  }

  .person { position: absolute; left: 38px; top: 232px; }
  .person__name { font-weight: 600; font-size: 24px; line-height: 1; color: var(--brand-blue); }
  .person__name .first { color: var(--brand-red); }
  .person__role { font-size: 14px; color: var(--ink); margin-top: 3px; }

  .divider {
    position: absolute; left: 38px; top: 277px; width: 524px; height: 1.5px;
    background: var(--brand-blue);
  }

  .contacts { position: absolute; left: 38px; top: 283px; list-style: none; }
  .contacts li {
    display: flex; align-items: center; gap: 8px;
    font-size: 14px; line-height: 18.5px; color: var(--ink);
  }
  .contacts svg { width: 13px; height: 13px; fill: var(--brand-blue); flex: none; }

  .address {
    position: absolute; right: 38px; top: 298px;
    font-size: 14px; line-height: 17px; color: var(--ink); font-style: normal;
  }

  .edge-stripe { position: absolute; left: 0; bottom: 0; width: 600px; height: 11px; }
</style>
</head>
<body>
<main class="canvas">
  <section class="card card--front">
    <div class="brand-name">BrightWove Care</div>

    <div class="person">
      <div class="person__name"><span class="first">Maren</span> Castell</div>
      <div class="person__role">Owner</div>
    </div>

    <div class="divider"></div>

    <ul class="contacts">
      <li>
        <svg viewBox="0 0 16 16" aria-hidden="true"><path d="M2 5c0-2 2-3 6-3s6 1 6 3v1h-3V5H5v1H2z"/><rect x="3" y="7" width="10" height="7" rx="1"/></svg>
        07 5182 2460
      </li>
      <li>
        <svg viewBox="0 0 16 16" aria-hidden="true"><path d="M1 3h14v10H1z M1 3l7 6 7-6" fill="none" stroke="#0c55a3" stroke-width="1.6"/><path d="M1 3h14L8 9z"/></svg>
        info@brightwovecare.com.au
      </li>
      <li>
        <svg viewBox="0 0 16 16" aria-hidden="true"><circle cx="8" cy="8" r="7"/><path d="M8 1v14M1 8h14" stroke="#fff" stroke-width="1"/></svg>
        www.brightwovecare.com.au
      </li>
    </ul>

    <address class="address">72 Meridian Road, Suite 204<br>Ashford, PA 18230</address>

    <svg class="edge-stripe" viewBox="0 0 600 11" preserveAspectRatio="none" aria-hidden="true">
      <polygon points="0,0 366,0 355,11 0,11" fill="var(--brand-blue)"/>
      <polygon points="374,0 600,0 600,11 363,11" fill="var(--brand-red)"/>
    </svg>
  </section>

  <section class="card card--back">
    <div class="brand-name brand-name--reverse">BrightWove Care</div>
  </section>
</main>
</body>
</html>
```